Professional Modern Website Design

We are a premium IT services provider to the financial industry based in London. Our company is called Veltra our current holding page is www.veltra-example.co.uk. We require a new website to match our new corporate identity. This project is for the design phase only. Development will be handled in-house. I have attached examples of wire frames we have developed (although open to suggestions for improvement) Our brand document that should demonstrate current brand, inc how we communicate to potential clients and finally mostly completed web-content.
We are looking for designers that can create something that sets us apart from our competitors.
Target Market(s)
IT Decision makers in Finance companies such as; hedge funds, private investment banks etc
Industry/Entity Type
Financial
Number of Pages Required
5+ page
Requirements
Must have
- hexagon elements in the design, unique design.
Nice to have
- Blog and social media feeds
Should not have
- Should not resemble a downloaded template

```html
<!DOCTYPE html>
<html lang="en">
<head>
<meta charset="utf-8">
<title>Veltra — IT Services for Finance</title>
<link href="https://fonts.googleapis.com/css2?family=Montserrat:wght@400;600;700&family=Open+Sans:wght@400;600&display=swap" rel="stylesheet">
<style>
:root{
  --orange:#f47b20;
  --orange-deep:#e8621a;
  --ink:#333333;
  --dark:#3b3b3b;
  --muted:#777777;
  --light:#f4f4f4;
  --line:#e2e2e2;
  --white:#ffffff;
}
*{box-sizing:border-box;margin:0;padding:0}
html,body{width:1200px;height:4541px;overflow:hidden}
body{position:relative;background:var(--white);font-family:"Open Sans",Arial,sans-serif;color:var(--ink)}
.abs{position:absolute}
.backdrop{position:absolute;left:0;top:0}
.heading{font-family:"Montserrat",Arial,sans-serif;font-weight:600;text-transform:uppercase;text-align:center;width:1200px;left:0}
.section-title{font-size:30px;color:var(--ink);letter-spacing:.5px}
.section-sub{font-size:12px;font-weight:600;color:var(--ink);letter-spacing:.5px}
.on-dark{color:var(--white)}
.section-icon{left:576px;width:48px;height:54px}
.arrow-badge{left:555px;width:90px;height:50px}
/* header */
.logo{left:210px;top:18px;display:flex;flex-direction:column;align-items:center;gap:6px}
.logo-mark{width:40px;height:40px;background:var(--orange)}
.logo-name{font-family:"Montserrat",Arial,sans-serif;font-weight:600;font-size:12px;letter-spacing:3px;color:var(--ink);text-transform:uppercase}
.nav{right:212px;top:40px;display:flex;gap:18px;font-family:"Montserrat",Arial,sans-serif;font-size:11px;font-weight:600;text-transform:uppercase;color:var(--ink)}
.nav .active{color:var(--orange);border-bottom:2px solid var(--orange);padding-bottom:4px}
/* hero */
.hero-art{left:690px;top:20px;width:510px;height:540px;background:radial-gradient(ellipse at 70% 45%,rgba(244,123,32,.55),rgba(244,123,32,.18) 55%,rgba(244,123,32,0) 75%)}
.hero-copy{left:210px;top:180px;width:430px}
.hero-kicker{font-family:"Montserrat",Arial,sans-serif;font-weight:700;font-size:22px;text-transform:uppercase;color:var(--ink)}
.hero-kicker em,.hero-title em{font-style:normal;color:var(--orange)}
.hero-title{font-family:"Montserrat",Arial,sans-serif;font-weight:700;font-size:34px;line-height:1.1;text-transform:uppercase;color:var(--ink);margin-top:2px}
.hero-text{font-size:14px;line-height:1.55;color:#555;margin-top:16px}
.btn{display:inline-block;font-family:"Montserrat",Arial,sans-serif;font-weight:600;font-size:11px;text-transform:uppercase;letter-spacing:.5px}
.btn-solid{background:var(--orange);color:var(--white);padding:13px 24px;margin-top:16px}
.btn-outline{border:1.5px solid var(--orange);color:var(--orange);padding:12px 26px}
/* welcome */
.welcome-text{left:210px;top:838px;width:780px;text-align:center;font-size:11px;line-height:1.75;color:var(--muted)}
/* services */
.service{position:absolute;width:256px;height:296px;clip-path:polygon(50% 0,100% 25%,100% 75%,50% 100%,0 75%,0 25%);background:var(--white);text-align:center;padding:70px 34px 0}
.service.featured{background:var(--dark)}
.service-icon{width:36px;height:36px;margin:0 auto 10px}
.service h3{font-family:"Montserrat",Arial,sans-serif;font-size:12px;font-weight:700;text-transform:uppercase;color:var(--orange);line-height:1.3}
.service.featured h3{color:var(--white)}
.service p{font-size:10.5px;line-height:1.55;color:var(--muted);margin-top:10px}
.service.featured p{color:#d8d8d8}
/* partners */
.partner{position:absolute;width:146px;height:168px;clip-path:polygon(50% 0,100% 25%,100% 75%,50% 100%,0 75%,0 25%);background:#ececec;display:flex;align-items:center;justify-content:center}
.partner::before{content:"";position:absolute;inset:2px;clip-path:polygon(50% 0,100% 25%,100% 75%,50% 100%,0 75%,0 25%);background:var(--white)}
.partner-badge{position:relative;width:70px;height:26px;background:#b9b9b9;border-radius:3px}
.partner.highlight{background:var(--orange)}
.partner.highlight::before{background:var(--orange)}
.partner.highlight .partner-badge{background:var(--white);opacity:.85}
/* testimonials */
.testimonial{position:absolute;width:374px}
.quote{background:var(--white);padding:18px 20px;font-size:11px;line-height:1.7;color:var(--muted);height:112px;box-shadow:0 1px 3px rgba(0,0,0,.06)}
.author{display:flex;align-items:center;gap:12px;margin-top:16px}
.avatar{width:44px;height:44px;border-radius:50%;background:radial-gradient(circle at 50% 40%,#f0b08a,#c97a55);border:2px solid var(--white)}
.author-name{font-size:12px;color:var(--orange);font-weight:600}
.author-role{font-size:10px;color:#999}
/* contact */
.contact-photo{left:0;top:3330px;width:1200px;height:720px;background:linear-gradient(100deg,#2e2e2e 0%,#3d3d3d 45%,#4b4845 70%,#3a3a3a 100%)}
.tweets{left:211px;top:3692px;width:440px;color:var(--white)}
.tweets h4{font-family:"Montserrat",Arial,sans-serif;font-size:13px;font-weight:700;text-transform:uppercase;margin-bottom:18px}
.tweet{display:flex;gap:14px;margin-bottom:22px;font-size:11px;line-height:1.65;color:#ddd}
.tweet-icon{flex:none;width:16px;height:16px;margin-top:2px}
.tweet a{color:var(--orange);text-decoration:none;font-weight:600}
.contact-form{left:702px;top:3694px;width:288px;display:flex;flex-direction:column;gap:12px}
.field{border:1px solid rgba(255,255,255,.45);height:38px;padding:10px 12px;font-size:11px;color:var(--white);background:rgba(0,0,0,.15)}
.field.tall{height:86px}
.submit{background:var(--white);color:var(--orange);height:38px;display:flex;align-items:center;justify-content:center;font-family:"Montserrat",Arial,sans-serif;font-size:11px;font-weight:700;text-transform:uppercase}
/* newsletter */
.newsletter{left:420px;top:4296px;width:360px;height:36px;display:flex}
.newsletter .input{flex:1;background:var(--white);font-size:10px;color:#999;padding:11px 14px;text-transform:uppercase}
.newsletter .go{width:100px;background:var(--dark);color:var(--white);font-family:"Montserrat",Arial,sans-serif;font-size:10px;font-weight:700;display:flex;align-items:center;justify-content:center;text-transform:uppercase}
.socials{left:0;width:1200px;top:4416px;display:flex;justify-content:center;gap:12px}
.social{width:40px;height:40px;border-radius:50%;background:var(--white);color:var(--orange);font-family:"Open Sans",Arial,sans-serif;font-weight:600;font-size:9px;display:flex;align-items:center;justify-content:center}
.copyright{left:0;width:1200px;top:4480px;text-align:center;font-size:10px;color:var(--white)}
</style>
</head>
<body>

<svg class="backdrop" width="1200" height="4541" viewBox="0 0 1200 4541" aria-hidden="true">
  <rect x="0" y="0" width="1200" height="470" fill="#f6f6f6"/>
  <polygon points="0,440 600,548 1200,440 1200,472 600,580 0,472" fill="#e6e6e6"/>
  <polygon points="0,1218 600,1072 1200,1218 1200,1818 600,1964 0,1818" fill="#f47b20"/>
  <polygon points="0,1218 600,1072 1200,1218 1200,1818 600,1964 0,1818" fill="none" stroke="#f9a25e" stroke-width="3"/>
  <polygon points="0,1240 600,1100 1200,1240 1200,1500 600,1400 0,1500" fill="#f68a35" opacity=".45"/>
  <rect x="0" y="3330" width="1200" height="720" fill="#3b3b3b"/>
  <polygon points="0,2800 600,2700 1200,2800 1200,3340 600,3448 0,3340" fill="#efefef"/>
  <rect x="0" y="3830" width="1200" height="711" fill="#f26522"/>
</svg>

<div class="abs contact-photo" role="img" aria-label="Photograph of a professional on the phone in an office, darkened behind the contact section"></div>
<svg class="backdrop" width="1200" height="4541" viewBox="0 0 1200 4541" aria-hidden="true">
  <polygon points="0,2800 600,2700 1200,2800 1200,3340 600,3448 0,3340" fill="#efefef"/>
  <polygon points="0,3830 600,4040 1200,3830 1200,3800 0,3800" fill="#3b3b3b" opacity="0"/>
</svg>
<svg class="backdrop" width="1200" height="4541" viewBox="0 0 1200 4541" aria-hidden="true" style="top:0">
  <polygon points="0,3840 1200,3840 1200,4541 0,4541" fill="#f26522"/>
  <polygon points="0,3838 600,4040 1200,3838" fill="#3b3b3b" opacity="0.92"/>
</svg>

<!-- Header -->
<header>
  <div class="abs logo"><span class="logo-mark"></span><span class="logo-name">Veltra</span></div>
  <nav class="abs nav">
    <span class="active">Home</span><span>About</span><span>Services</span><span>Partners</span><span>Clients</span><span>Contact</span>
  </nav>
</header>

<!-- Hero -->
<section class="hero">
  <div class="abs hero-art" role="img" aria-label="Decorative cluster of orange geometric shapes"></div>
  <div class="abs hero-copy">
    <p class="hero-kicker">You need <em>integration</em></p>
    <h1 class="hero-title">We're always<br>there <em>with</em> you</h1>
    <p class="hero-text">Veltra is one of the leading systems integrators to the world's finance sector. We are an extension of your business and our services portfolio has been built so you always have access to a complete partner.</p>
    <span class="btn btn-solid">Learn more</span>
  </div>
</section>

<svg class="abs arrow-badge" style="top:568px" viewBox="0 0 90 50" aria-hidden="true"><polygon points="14,0 76,0 90,25 76,50 14,50 0,25" fill="#f47b20"/><polyline points="36,18 45,28 54,18" fill="none" stroke="#fff" stroke-width="3"/></svg>

<!-- Welcome -->
<section class="welcome">
  <svg class="abs section-icon" style="top:704px" viewBox="0 0 48 54" aria-hidden="true"><polygon points="24,2 46,14 46,40 24,52 2,40 2,14" fill="none" stroke="#f47b20" stroke-width="2"/><circle cx="24" cy="27" r="7" fill="none" stroke="#f47b20" stroke-width="2.5"/></svg>
  <h2 class="abs heading section-title" style="top:762px">Welcome to Veltra</h2>
  <p class="abs heading section-sub" style="top:800px">Veltra is committed to customers</p>
  <p class="abs welcome-text">We help finance firms plan, build and run the technology that keeps trading desks, risk teams and back offices moving. From secure data centres to managed support, our engineers work alongside your own people, learn how your business operates and stay with you long after a project goes live. Every engagement starts with listening, and every solution is designed around resilience, compliance and the pace of the markets you serve. Clients rely on us for clear advice, honest pricing and a team that answers the phone.</p>
  <span class="abs btn btn-outline" style="left:529px;top:946px">Learn more</span>
</section>

<svg class="abs arrow-badge" style="top:1084px" viewBox="0 0 90 50" aria-hidden="true"><polygon points="14,0 76,0 90,25 76,50 14,50 0,25" fill="#fff"/><polyline points="36,18 45,28 54,18" fill="none" stroke="#f47b20" stroke-width="3"/></svg>

<!-- Services -->
<section class="services">
  <svg class="abs section-icon" style="top:1204px" viewBox="0 0 48 54" aria-hidden="true"><polygon points="24,2 46,14 46,40 24,52 2,40 2,14" fill="none" stroke="#fff" stroke-width="2"/><circle cx="24" cy="27" r="7" fill="none" stroke="#fff" stroke-width="2.5"/></svg>
  <h2 class="abs heading section-title on-dark" style="top:1264px">Veltra Services</h2>
  <p class="abs heading section-sub on-dark" style="top:1302px">The Veltra key pillars</p>

  <div class="service" style="left:209px;top:1328px">
    <svg class="service-icon" viewBox="0 0 36 36" aria-hidden="true"><ellipse cx="18" cy="8" rx="11" ry="4" fill="#555"/><rect x="7" y="8" width="22" height="18" fill="#555"/><ellipse cx="18" cy="26" rx="11" ry="4" fill="#555"/></svg>
    <h3>Data centre and infrastructure solutions</h3>
    <p>Veltra offers design, deployment, implementation and management of your infrastructure to boost your company's productivity and profitability.</p>
  </div>
  <div class="service featured" style="left:472px;top:1328px">
    <svg class="service-icon" viewBox="0 0 36 36" aria-hidden="true"><circle cx="18" cy="18" r="14" fill="#fff"/><circle cx="18" cy="18" r="9" fill="none" stroke="#3b3b3b" stroke-width="2"/></svg>
    <h3>IT support, managed &amp; professional services</h3>
    <p>Veltra built its reputation on IT support, management and professional services and continues to operate with these as a priority.</p>
  </div>
  <div class="service" style="left:735px;top:1328px">
    <svg class="service-icon" viewBox="0 0 36 36" aria-hidden="true"><ellipse cx="18" cy="8" rx="11" ry="4" fill="#555"/><rect x="7" y="8" width="22" height="18" fill="#555"/><ellipse cx="18" cy="26" rx="11" ry="4" fill="#555"/></svg>
    <h3>Voice &amp; data networks</h3>
    <p>Veltra can offer flexible fixed-line or VoIP telephony to create an IP platform based around a flexible, mobile and agile workforce.</p>
  </div>
  <div class="service" style="left:342px;top:1588px">
    <svg class="service-icon" viewBox="0 0 36 36" aria-hidden="true"><ellipse cx="18" cy="8" rx="11" ry="4" fill="#555"/><rect x="7" y="8" width="22" height="18" fill="#555"/><ellipse cx="18" cy="26" rx="11" ry="4" fill="#555"/></svg>
    <h3>Hosting and cloud</h3>
    <p>Veltra can help you harness the value of highly secure hosting and cloud solutions to make data safe and processes efficient.</p>
  </div>
  <div class="service" style="left:605px;top:1588px">
    <svg class="service-icon" viewBox="0 0 36 36" aria-hidden="true"><ellipse cx="18" cy="8" rx="11" ry="4" fill="#555"/><rect x="7" y="8" width="22" height="18" fill="#555"/><ellipse cx="18" cy="26" rx="11" ry="4" fill="#555"/></svg>
    <h3>Information technology security &amp; GRC</h3>
    <p>Veltra offers specialised information and cyber security management. We know how important protection is to your whole organisation.</p>
  </div>
</section>

<svg class="abs arrow-badge" style="top:1944px" viewBox="0 0 90 50" aria-hidden="true"><polygon points="14,0 76,0 90,25 76,50 14,50 0,25" fill="#fff"/><polyline points="36,18 45,28 54,18" fill="none" stroke="#f47b20" stroke-width="3"/></svg>

<!-- Partners -->
<section class="partners">
  <svg class="abs section-icon" style="top:2082px" viewBox="0 0 48 54" aria-hidden="true"><polygon points="24,2 46,14 46,40 24,52 2,40 2,14" fill="none" stroke="#f47b20" stroke-width="2"/><circle cx="24" cy="27" r="7" fill="none" stroke="#f47b20" stroke-width="2.5"/></svg>
  <h2 class="abs heading section-title" style="top:2138px">Veltra Partners</h2>
  <p class="abs heading section-sub" style="top:2176px">Integrated partnerships</p>

  <div class="partner" style="left:203px;top:2244px"><span class="partner-badge"></span></div>
  <div class="partner" style="left:365px;top:2244px"><span class="partner-badge"></span></div>
  <div class="partner" style="left:527px;top:2244px"><span class="partner-badge"></span></div>
  <div class="partner" style="left:689px;top:2244px"><span class="partner-badge"></span></div>
  <div class="partner" style="left:851px;top:2244px"><span class="partner-badge"></span></div>
  <div class="partner" style="left:284px;top:2386px"><span class="partner-badge"></span></div>
  <div class="partner highlight" style="left:446px;top:2386px"><span class="partner-badge"></span></div>
  <div class="partner" style="left:608px;top:2386px"><span class="partner-badge"></span></div>
  <div class="partner" style="left:770px;top:2386px"><span class="partner-badge"></span></div>
</section>

<svg class="abs arrow-badge" style="top:2650px" viewBox="0 0 90 50" aria-hidden="true"><polygon points="14,0 76,0 90,25 76,50 14,50 0,25" fill="#f47b20"/><polyline points="36,18 45,28 54,18" fill="none" stroke="#fff" stroke-width="3"/></svg>

<!-- Testimonials -->
<section class="testimonials">
  <svg class="abs section-icon" style="top:2756px" viewBox="0 0 48 54" aria-hidden="true"><polygon points="24,2 46,14 46,40 24,52 2,40 2,14" fill="none" stroke="#f47b20" stroke-width="2"/><rect x="15" y="20" width="18" height="13" rx="2" fill="#f47b20"/></svg>
  <h2 class="abs heading section-title" style="top:2812px">Client Testimonials</h2>
  <p class="abs heading section-sub" style="top:2850px">What our client says about us</p>

  <div class="testimonial" style="left:211px;top:2919px">
    <p class="quote">Veltra moved our entire trading floor to a new data centre over one weekend without a single minute of lost trading. Their engineers planned every step and kept us informed throughout.</p>
    <div class="author"><span class="avatar"></span><div><p class="author-name">– Dale Armitage</p><p class="author-role">Head of IT, Westbrook Capital</p></div></div>
  </div>
  <div class="testimonial" style="left:616px;top:2919px">
    <p class="quote">The support desk knows our systems as well as we do. Issues are picked up quickly, explained clearly and fixed properly, which lets my team focus on the projects that matter.</p>
    <div class="author"><span class="avatar"></span><div><p class="author-name">– Dale Armitage</p><p class="author-role">Head of IT, Westbrook Capital</p></div></div>
  </div>
  <div class="testimonial" style="left:211px;top:3140px">
    <p class="quote">We needed a partner who understood regulation as well as technology. Veltra delivered a secure cloud platform that passed our audit first time and scales with the fund.</p>
    <div class="author"><span class="avatar"></span><div><p class="author-name">– Dale Armitage</p><p class="author-role">Head of IT, Westbrook Capital</p></div></div>
  </div>
  <div class="testimonial" style="left:616px;top:3140px">
    <p class="quote">From the first meeting they listened. The new voice and data network is faster, cheaper to run and gives our analysts the freedom to work from anywhere.</p>
    <div class="author"><span class="avatar"></span><div><p class="author-name">– Dale Armitage</p><p class="author-role">Head of IT, Westbrook Capital</p></div></div>
  </div>
</section>

<svg class="abs arrow-badge" style="top:3406px" viewBox="0 0 90 50" aria-hidden="true"><polygon points="14,0 76,0 90,25 76,50 14,50 0,25" fill="#f47b20"/><polyline points="36,18 45,28 54,18" fill="none" stroke="#fff" stroke-width="3"/></svg>

<!-- Contact -->
<section class="contact">
  <svg class="abs section-icon" style="top:3530px" viewBox="0 0 48 54" aria-hidden="true"><polygon points="24,2 46,14 46,40 24,52 2,40 2,14" fill="none" stroke="#f47b20" stroke-width="2"/><path d="M17 19c2-1 3 0 4 2l-1 3c1 2 3 4 5 5l3-1c2 1 3 2 2 4-1 2-3 3-5 2-5-2-9-6-10-11 0-2 1-3 2-4z" fill="#f47b20"/></svg>
  <h2 class="abs heading section-title on-dark" style="top:3590px">Get in touch</h2>
  <p class="abs heading section-sub on-dark" style="top:3628px">Contact information</p>

  <div class="abs tweets">
    <h4>Latest tweets</h4>
    <div class="tweet"><svg class="tweet-icon" viewBox="0 0 16 16" aria-hidden="true"><circle cx="8" cy="8" r="7" fill="#fff"/></svg><p>New guide out today: five steps to a resilient trading infrastructure. Practical advice for IT leads in hedge funds and investment banks. <a>Read More</a></p></div>
    <div class="tweet"><svg class="tweet-icon" viewBox="0 0 16 16" aria-hidden="true"><circle cx="8" cy="8" r="7" fill="#fff"/></svg><p>Our security team will be speaking at next month's finance technology forum in London. Come and say hello at our stand. <a>Read More</a></p></div>
    <div class="tweet"><svg class="tweet-icon" viewBox="0 0 16 16" aria-hidden="true"><circle cx="8" cy="8" r="7" fill="#fff"/></svg><p>We are hiring engineers who love solving hard problems for demanding clients. See the latest roles on our careers page. <a>Read More</a></p></div>
  </div>

  <div class="abs contact-form">
    <div class="field">Full Name</div>
    <div class="field">Phone Number</div>
    <div class="field">Email Address</div>
    <div class="field tall">Your Message</div>
    <div class="submit">Submit</div>
  </div>
</section>

<svg class="abs arrow-badge" style="top:4030px" viewBox="0 0 90 50" aria-hidden="true"><polygon points="14,0 76,0 90,25 76,50 14,50 0,25" fill="#fff"/><polyline points="36,18 45,28 54,18" fill="none" stroke="#f47b20" stroke-width="3"/></svg>

<!-- Newsletter / footer -->
<footer>
  <svg class="abs section-icon" style="top:4156px" viewBox="0 0 48 54" aria-hidden="true"><polygon points="24,2 46,14 46,40 24,52 2,40 2,14" fill="none" stroke="#fff" stroke-width="2"/><rect x="14" y="20" width="20" height="14" fill="none" stroke="#fff" stroke-width="2"/><polyline points="14,20 24,28 34,20" fill="none" stroke="#fff" stroke-width="2"/></svg>
  <h2 class="abs heading section-title on-dark" style="top:4216px">Subscribe to our newsletter</h2>
  <p class="abs heading section-sub on-dark" style="top:4254px">Subscribe newsletter to get offers</p>
  <div class="abs newsletter"><span class="input">Enter email id</span><span class="go">Subscribe</span></div>
  <div class="abs socials">
    <span class="social">Pulse</span><span class="social">Chirp</span><span class="social">Linkup</span><span class="social">Orbit</span>
  </div>
  <p class="abs copyright">Copyright © 2015 Veltra. All Rights reserved.</p>
</footer>

</body>
</html>
```